Brightmoor Glowing - Two Pages of Information and Pictures

We need a two page summary of the Service Offerings of Brightmoor Glowing - a company that installs LED Lighting. We've written the copy and picked images and chart that we like and have laid it out a word document.

We're looking for someone to design a more professional page layout than the generic Word Template. Please do not feel the current layout is suggested. It is only laid out this way because Word had that template. Be as creative as you want.

We would like the images and text to be in the same order that it is in now.

We're also in a rush so speed is appreciated. THANK YOU !!

Target Market(s)

Corporate Offices in New York

Industry/Entity Type

Lighting Fixture

Colors
85cae6
87cfc7
9bcb3c
3377b5

Requirements
Must have
• Must include two pages of the copy and images written and provided in the word document that was uploaded. Must use the Brightmoor colors in the logo.
Nice to have
• An easy to read flow of images and.

```html
<!DOCTYPE html>
<html lang="en">
<head>
<meta charset="utf-8">
<title>Brightmoor Glowing – Service Overview</title>
<link href="https://fonts.googleapis.com/css2?family=Open+Sans:wght@300;400;600;700&family=Signika:wght@500;600&display=swap" rel="stylesheet">
<style>
  :root{
    --sky:#85cae6;
    --teal:#87cfc7;
    --green:#9bcb3c;
    --band-green:#7cc142;
    --title-green:#5da530;
    --blue:#3377b5;
    --ink:#444;
    --grey-band:#5e5f61;
    --backdrop:#e9e6e1;
    --white:#fff;
  }
  *{box-sizing:border-box;margin:0;padding:0}
  html,body{width:1200px;height:1200px;overflow:hidden;background:var(--backdrop);font-family:"Open Sans",Arial,sans-serif;color:var(--ink)}
  .page{position:absolute;top:237px;width:672px;height:870px;background:var(--white);transform:scale(.8333);transform-origin:top left;box-shadow:0 3px 14px rgba(0,0,0,.18);overflow:hidden}
  .page--front{left:20px}
  .page--back{left:620px}
  .abs{position:absolute}
  .photo{position:absolute;border:1px solid var(--title-green)}

  /* front */
  .brand{left:0;top:0;width:412px;height:162px;display:flex;flex-direction:column;align-items:center;justify-content:center}
  .brand__name{font-family:"Open Sans",sans-serif;font-weight:400;font-size:20px;letter-spacing:2px;color:var(--blue);display:flex;align-items:center;gap:10px}
  .brand__mark{width:14px;height:14px;background:var(--teal)}
  .brand__tagline{margin-top:26px;font-weight:300;font-size:15px;color:#333}
  .offer{left:0;top:655px;width:672px;height:178px;background:var(--band-green);text-align:center;padding:40px 38px 0}
  .offer__title{font-family:"Signika",sans-serif;font-weight:600;font-size:35px;color:var(--blue);letter-spacing:.3px}
  .offer__text{margin-top:14px;font-size:9.2px;line-height:12px;color:var(--white)}
  .site-bar{left:0;top:833px;width:672px;height:37px;background:var(--blue);color:#dfe9f4;font-size:10px;letter-spacing:6px;text-align:center;line-height:37px}

  /* back */
  .section-title{font-weight:700;font-size:13px}
  .section-title--green{color:var(--title-green)}
  .section-title--blue{color:var(--blue)}
  .savings-table{left:40px;top:62px;width:592px;border-collapse:collapse;font-size:7.4px;color:#333}
  .savings-table th{background:var(--blue);color:var(--white);font-weight:400;height:20px;border-left:1px solid #5f93c5}
  .savings-table th:first-child{border-radius:6px 0 0 0;border-left:none}
  .savings-table th:last-child{border-radius:0 6px 0 0}
  .savings-table td{height:22px;border:1px solid #b7c9e1;text-align:center;padding:0 2px}
  .savings-table td.label{text-align:left;padding-left:6px}
  .rate-note{left:198px;top:153px;font-size:7px}
  .chart{left:40px;top:177px;width:296px;height:184px;border:1px solid #bbb}
  .body-copy{font-size:8.6px;line-height:11.8px;text-align:justify;color:#555}
  .body-copy p+p{margin-top:7px}
  .testimonials{left:0;top:570px;width:672px;height:220px;background:var(--grey-band)}
  .testimonials__title{position:absolute;top:6px;width:100%;text-align:center;color:var(--band-green);font-size:20px;font-weight:600}
  .testimonials__frame{position:absolute;left:40px;top:34px;width:592px;height:168px;border:1px solid #c9c9c9;border-radius:8px}
  .quote-mark{position:absolute;font-family:"Signika",sans-serif;font-weight:600;font-size:28px;color:var(--band-green);background:var(--grey-band);padding:0 4px;line-height:24px}
  .quote{position:absolute;left:14px;width:566px;font-size:8.6px;line-height:11.5px;color:var(--white)}
  .quote__source{display:block;text-align:right;color:var(--band-green);margin-top:5px}
  .contact{left:0;top:790px;width:672px;height:45px;display:flex;align-items:center;justify-content:center;gap:20px;font-size:15px;color:#222}
  .contact span{display:flex;align-items:center;gap:6px}
</style>
</head>
<body>

<section class="page page--front">
  <div class="brand abs">
    <div class="brand__name"><span class="brand__mark"></span>BRIGHTMOOR</div>
    <div class="brand__tagline">Making LEDs beautiful.</div>
  </div>

  <div class="photo" style="left:413px;top:0;width:259px;height:152px;background:linear-gradient(180deg,#c9c4bb,#6d6a66)" role="img" aria-label="Office staircase with lit display wall"></div>
  <div class="photo" style="left:0;top:162px;width:404px;height:488px;background:linear-gradient(160deg,#3b2a1c,#a5662c 55%,#c58a4a)" role="img" aria-label="Warm lit showroom with wooden walls and white dining table"></div>
  <div class="photo" style="left:413px;top:162px;width:259px;height:153px;background:linear-gradient(150deg,#d7c7a4,#8a7a5f)" role="img" aria-label="Pendant filament LED bulbs in an office"></div>
  <div class="photo" style="left:413px;top:325px;width:259px;height:153px;background:linear-gradient(180deg,#f1f1ee,#b8b8b2)" role="img" aria-label="Bright open plan office"></div>
  <div class="photo" style="left:413px;top:488px;width:259px;height:162px;background:linear-gradient(180deg,#f5f5f2,#5a5a58)" role="img" aria-label="Classroom with rows of desks under LED lighting"></div>

  <div class="offer abs">
    <h1 class="offer__title">No Upfront Cost-TURNKEY LEDS</h1>
    <p class="offer__text">Brightmoor Glowing provides LED lighting as a service – fully implemented and managed LEDs at no upfront cost. Brightmoor takes the risk, hassle and capital cost out of adopting LED's energy saving technology. Brightmoor guarantees net-savings for customers on day one, and continues to guarantee savings and performance for the full term of the contract. And the savings add up! A project can be installed 2-4 weeks from kickoff, and projects continue to generate savings for up to 10 years.</p>
  </div>
  <div class="site-bar abs">WWW.BRIGHTMOORGLOWING.COM</div>
</section>

<section class="page page--back">
  <h2 class="section-title section-title--green abs" style="left:40px;top:36px">Why use Brightmoor?</h2>

  <table class="savings-table abs">
    <tr><th style="width:30px">250000</th><th style="width:22px">FT2</th><th style="width:98px">YEAR</th><th>1</th><th>2</th><th>3</th><th>4</th><th>5</th><th>6</th><th>7</th><th>8</th><th>9</th><th>10</th></tr>
    <tr><td>0.04</td><td>$/ft2</td><td class="label">Annual Brightmoor Service</td><td>$100,000</td><td>$100,000</td><td>$100,000</td><td>$100,000</td><td>$100,000</td><td></td><td></td><td></td><td></td><td></td></tr>
    <tr><td>0.08</td><td>$/ft2</td><td class="label">Annual Net-Savings</td><td>$140,000</td><td>$140,000</td><td>$140,000</td><td>$140,000</td><td>$140,000</td><td>$240,000</td><td>$240,000</td><td>$240,000</td><td>$240,000</td><td>$240,000</td></tr>
    <tr><td></td><td></td><td class="label">Total Net-Savings</td><td>$140,000</td><td>$280,000</td><td>$420,000</td><td>$560,000</td><td>$700,000</td><td>$940,000</td><td>$1,180,000</td><td>$1,420,000</td><td>$1,660,000</td><td>$1,900,000</td></tr>
  </table>
  <div class="rate-note abs">$0.0467</div>

  <svg class="chart abs" viewBox="0 0 296 184" font-family="Open Sans, sans-serif">
    <text x="148" y="17" font-size="8" text-anchor="middle" fill="#333">Annual and Total Net-Savings of 250,000 ft2 Customer</text>
    <g font-size="4" fill="#555" text-anchor="end">
      <text x="38" y="30">$300</text><text x="38" y="50">$250</text><text x="38" y="71">$200</text><text x="38" y="91">$150</text><text x="38" y="112">$100</text><text x="38" y="132">$50</text><text x="38" y="153">$-</text>
    </g>
    <g font-size="4" fill="#555">
      <text x="262" y="30">$2.0</text><text x="262" y="55">$1.6</text><text x="262" y="79">$1.2</text><text x="262" y="104">$0.8</text><text x="262" y="128">$0.4</text><text x="262" y="153">$0.0</text>
    </g>
    <line x1="42" y1="151" x2="258" y2="151" stroke="#bbb" stroke-width=".6"/>
    <g fill="var(--teal)">
      <rect x="47" y="110" width="5" height="41"/><rect x="69" y="110" width="5" height="41"/><rect x="91" y="110" width="5" height="41"/><rect x="113" y="110" width="5" height="41"/><rect x="135" y="110" width="5" height="41"/>
    </g>
    <g fill="var(--green)">
      <rect x="53" y="94" width="6" height="57"/><rect x="75" y="94" width="6" height="57"/><rect x="97" y="94" width="6" height="57"/><rect x="119" y="94" width="6" height="57"/><rect x="141" y="94" width="6" height="57"/>
      <rect x="161" y="53" width="6" height="98"/><rect x="183" y="53" width="6" height="98"/><rect x="205" y="53" width="6" height="98"/><rect x="227" y="53" width="6" height="98"/><rect x="249" y="53" width="6" height="98"/>
    </g>
    <polyline points="53,143 75,134 97,125 119,117 141,108 163,94 185,79 207,64 229,50 251,35" fill="none" stroke="#777" stroke-width=".8"/>
    <g font-size="4" fill="#555" text-anchor="middle">
      <text x="53" y="158">1</text><text x="75" y="158">2</text><text x="97" y="158">3</text><text x="119" y="158">4</text><text x="141" y="158">5</text><text x="163" y="158">6</text><text x="185" y="158">7</text><text x="207" y="158">8</text><text x="229" y="158">9</text><text x="251" y="158">10</text>
    </g>
    <g font-size="3.8" fill="#555">
      <rect x="58" y="168" width="10" height="2" fill="var(--teal)"/><text x="70" y="171">Annual Brightmoor Service</text>
      <rect x="133" y="168" width="10" height="2" fill="var(--green)"/><text x="145" y="171">Annual Net-Savings</text>
      <rect x="195" y="168.5" width="10" height="1" fill="#777"/><text x="207" y="171">Total Net-Savings</text>
    </g>
  </svg>

  <div class="body-copy abs" style="left:356px;top:175px;width:276px">
    <p>with the risk, hassle and capital cost on their own. Brightmoor starts saving customers money the first month – typically a netsavings of about 4.7 cents a square-foot per month. Brightmoor will design aesthetic LED systems and install the best available technology.</p>
    <p>Brightmoor provides LEDs at the best cost with its as-a-service structure, which puts the cost of lighting into clients' monthly operating budget for less than they save. By installing projects immediately, Brightmoor eliminates the cost of foregone savings that would accumulate from delayed implementation.</p>
    <p>It can be risky to adopt new technology, especially when salespeople try to sell more than is needed. Brightmoor has access to better equipment and at better cost than is widely available on the open market and passes that quality and savings on to its customers. Brightmoor guarantees performance for 5 years, which removes the risk of a failed project.</p>
  </div>

  <h2 class="section-title section-title--blue abs" style="left:40px;top:385px">The Best Team in LEDs :</h2>
  <div class="body-copy abs" style="left:40px;top:410px;width:297px">
    <p>Brightmoor is a team of lighting experts who get the evolution of lighting and efficiency.</p>
    <p style="margin-top:14px">Simply put, we come in up every day with one goal: to provide an excellent service that saves money and uses less electricity. Part of the team focuses on the supply chain of the very best equipment that customers have come to appreciate. Part of the team focuses on the project management of each installation. And, part of the team focuses on resolving any questions customers might have in their transition. Together we make up the best team in LEDs and work tirelessly to make it easy to upgrade.</p>
  </div>
  <div class="photo" style="left:356px;top:388px;width:276px;height:151px;border-color:#ccc;background:linear-gradient(160deg,#5c6b3a,#4b6a93 55%,#2f3a4a)" role="img" aria-label="Team members in branded t-shirts seen from behind in a garden"></div>

  <div class="testimonials abs">
    <h2 class="testimonials__title">Testimonials</h2>
    <div class="testimonials__frame">
      <span class="quote-mark" style="left:6px;top:-13px">“</span>
      <span class="quote-mark" style="right:6px;bottom:-14px">”</span>
      <p class="quote" style="top:9px">Brightmoor made a huge improvement in the lighting for our headquarters. The installation process was as smooth as can be and the service since has been excellent.<span class="quote__source">Harborline Health</span></p>
      <p class="quote" style="top:59px">In a museum, quality lighting is paramount. Brightmoor has been a great partner in helping us transition to LEDs that look great, save us money, and make lighting management so much simpler.<span class="quote__source">Riverside Kids Art Museum, New York</span></p>
      <p class="quote" style="top:112px">We are so happy to have had Brightmoor's help building out our new office space – they put their lighting expertise to work delivering beautiful LEDs and fixtures. It was cost-effective, removed lighting from the build-out budget, and it's been a joy to work with them since.<span class="quote__source" style="margin-top:2px">Lanterncraft, Inc</span></p>
    </div>
  </div>

  <div class="contact abs">
    <span><svg width="13" height="13" viewBox="0 0 24 24"><path d="M6.6 10.8a15.1 15.1 0 0 0 6.6 6.6l2.2-2.2c.3-.3.7-.4 1-.2 1.1.4 2.3.6 3.6.6.6 0 1 .4 1 1V20c0 .6-.4 1-1 1A17 17 0 0 1 3 4c0-.6.4-1 1-1h3.5c.6 0 1 .4 1 1 0 1.3.2 2.5.6 3.6.1.3 0 .7-.2 1z" fill="var(--band-green)"/></svg>555 010 GLOW</span>
    <span><svg width="15" height="12" viewBox="0 0 24 18"><rect x="1" y="1" width="22" height="16" rx="2" fill="var(--band-green)"/><path d="M2 2l10 8 10-8" fill="none" stroke="#fff" stroke-width="2"/></svg>customers@brightmoorglowing.com</span>
  </div>
  <div class="site-bar abs">WWW.BRIGHTMOORGLOWING.COM</div>
</section>

</body>
</html>
```